Chewable Dog Supplements jar with lid

Below are some specifications of this project: 
There will be 6 different types of dog supplements in different jars, which will have different colors, or elements(dogs),  but will respect the same theme overall.  I attached some pictures below as a reference.
 The design I would like to create is for a label that will go around and on the top of a round plastic jar. The size of the product label is 25cm long and 8.5 cm high and on the top there is a circle that goes on the lid with the exact same design as on the front.
Some small pictures on the back with no Grain, Corn or Soy derivates  
 All products come in different shapes chews 
All products have 3 different headlines with their benefits that go on the front of the design.
All products have different flavors.
Regarding the text that will go on the back of the product, I can help with adding that to all products as long as we agree on how it looks. On the back I will need a space for a barcode, best before date, there should be 2 tables with ingredients and directions for use, and space for text under :Storage instructions, Warning, Description.

Target Market(s)

Europe

Industry/Entity Type

pet food

Requirements
Must have
• Trust signals ( Free from GMO, Natural ingredients, Free from artificial colouring) and a text box with the benefits of the product that I will provide.

```html
<!DOCTYPE html>
<html lang="en">
<head>
<meta charset="utf-8">
<title>Pawnova Chews Labels</title>
<link href="https://fonts.googleapis.com/css2?family=Fredoka:wght@600&family=Roboto+Condensed:wght@400;700&family=Montserrat:wght@500&display=swap" rel="stylesheet">
<style>
  :root{
    --bg:#6b6b6b;
    --white:#ffffff;
    --ink:#1b1b1b;
    --green-main:#3db245;
    --green-deep:#2a9631;
    --green-lime:#b4e81c;
    --green-bullet:#c8f03a;
    --blue-main:#3cb2df;
    --blue-deep:#2a4fc0;
    --blue-paw:#2f62d2;
    --blue-bullet:#1f3f9e;
  }
  *{box-sizing:border-box;margin:0;padding:0}
  html,body{width:1200px;height:1200px;overflow:hidden;background:var(--bg)}
  .stage{position:relative;width:1200px;height:1200px}
  .label{position:absolute;top:484px;width:490px;height:348px;overflow:hidden;
    background:var(--main);font-family:"Roboto Condensed",sans-serif;color:var(--white)}
  .label--multivitamin{left:57px;--main:var(--green-main);--deep:var(--green-deep);--band:var(--green-lime);--bullet:var(--green-bullet);--band-ink:var(--ink)}
  .label--calming{left:654px;--main:var(--blue-main);--deep:var(--blue-paw);--band:var(--blue-deep);--bullet:var(--blue-bullet);--band-ink:var(--white)}
  .brand{position:absolute;top:28px;left:0;width:100%;text-align:center;font-family:"Montserrat",sans-serif;
    font-weight:500;font-size:11px;letter-spacing:4px}
  .brand__dot{display:block;width:26px;height:26px;border:2px solid var(--white);border-radius:50%;margin:0 auto 14px}
  .title{position:absolute;top:92px;left:0;width:100%;text-align:center;font-family:"Fredoka",sans-serif;
    font-weight:600;font-size:44px;line-height:1;letter-spacing:.5px}
  .benefits{position:absolute;top:162px;left:47px;list-style:none;font-size:16px;line-height:22px}
  .benefits li{display:flex;align-items:center;gap:6px}
  .benefits li::before{content:"";width:11px;height:6px;border-radius:3px;background:var(--bullet)}
  .badges{position:absolute;top:233px;left:50px;display:flex;gap:6px}
  .badge{width:35px;height:35px;border:1.5px solid var(--white);border-radius:50%}
  .dog-photo{position:absolute;left:292px;top:143px;width:124px;height:158px;border-radius:40px 40px 8px 8px}
  .label--multivitamin .dog-photo{background:linear-gradient(180deg,#2b2b2b 0%,#4a4a4a 55%,#e9e6e0 100%)}
  .label--calming .dog-photo{background:linear-gradient(180deg,#d8a968 0%,#e6c290 55%,#f1dcb8 100%)}
  .paw-area{position:absolute;left:290px;top:150px;width:180px;height:170px;border-radius:50%;background:var(--deep);opacity:.55}
  .arrow{position:absolute;left:190px;top:198px}
  .chews-photo{position:absolute;left:193px;top:245px;width:105px;height:69px;border-radius:30px;
    background:linear-gradient(160deg,#e6d6a8 0%,#cbb27a 60%,#7a5a34 100%)}
  .band{position:absolute;left:0;bottom:0}
  .support{position:absolute;left:56px;top:318px;font-size:10px;color:var(--band-ink);
    border-bottom:1px solid var(--band-ink);padding-bottom:1px}
  .count{position:absolute;left:200px;top:322px;width:90px;text-align:center;color:var(--band-ink)}
  .count__main{font-weight:700;font-size:13px;line-height:1}
  .count__net{font-size:5.5px;line-height:1}
  .flavor{position:absolute;left:357px;top:312px;width:78px;height:29px;border:1px solid var(--band-ink);display:flex}
  .flavor__icon{width:38px;display:flex;align-items:center;justify-content:center}
  .flavor__name{flex:1;font-weight:700;font-size:9.5px;line-height:9px;display:flex;align-items:center;justify-content:center;text-align:center}
  .label--multivitamin .flavor__name{background:var(--ink);color:var(--green-lime)}
  .label--calming .flavor__name{background:var(--white);color:var(--blue-deep)}
</style>
</head>
<body>
<main class="stage">

  <section class="label label--multivitamin">
    <div class="paw-area"></div>
    <div class="brand"><span class="brand__dot"></span>PAWNOVA</div>
    <h1 class="title">MULTIVITAMIN CHEWS</h1>
    <ul class="benefits">
      <li>Strong inmunity</li>
      <li>Hip and joint support</li>
      <li>Skin and coat health</li>
    </ul>
    <div class="badges"><span class="badge"></span><span class="badge"></span><span class="badge"></span></div>
    <svg class="arrow" width="60" height="45" viewBox="0 0 60 45"><path d="M4 8 Q40 0 50 34" fill="none" stroke="var(--green-bullet)" stroke-width="3.5" stroke-linecap="round"/><path d="M41 28 L50 38 L56 26" fill="none" stroke="var(--green-bullet)" stroke-width="3.5" stroke-linecap="round" stroke-linejoin="round"/></svg>
    <svg class="band" width="490" height="64" viewBox="0 0 490 64"><path d="M0 16 Q40 0 90 14 Q140 28 200 12 Q250 0 300 14 Q360 30 420 12 Q460 2 490 14 L490 64 L0 64 Z" fill="var(--band)"/></svg>
    <div class="dog-photo" role="img" aria-label="Photo of a black and white border collie"></div>
    <div class="chews-photo" role="img" aria-label="Photo of three filled chew treats"></div>
    <span class="support">SUPOPORT FOR DOG</span>
    <div class="count"><div class="count__main">60 CHEWS</div><div class="count__net">NET WT 5.29 oz (150g)</div></div>
    <div class="flavor">
      <span class="flavor__icon"><svg width="28" height="16" viewBox="0 0 28 16"><path d="M2 8 Q12 0 22 8 Q12 16 2 8 Z M22 8 L27 3 L27 13 Z" fill="none" stroke="var(--ink)" stroke-width="1.4"/><circle cx="8" cy="7" r="1" fill="var(--ink)"/></svg></span>
      <span class="flavor__name">SALMON<br>FLAVOR</span>
    </div>
  </section>

  <section class="label label--calming">
    <div class="paw-area"></div>
    <div class="brand"><span class="brand__dot"></span>PAWNOVA</div>
    <h1 class="title">CALMING CHEWS</h1>
    <ul class="benefits">
      <li>Helps manage normal stress</li>
      <li>Promotes relaxation</li>
      <li>Helps restless dogs</li>
    </ul>
    <div class="badges"><span class="badge"></span><span class="badge"></span><span class="badge"></span></div>
    <svg class="arrow" width="60" height="45" viewBox="0 0 60 45"><path d="M4 8 Q40 0 50 34" fill="none" stroke="#152a6e" stroke-width="3.5" stroke-linecap="round"/><path d="M41 28 L50 38 L56 26" fill="none" stroke="#152a6e" stroke-width="3.5" stroke-linecap="round" stroke-linejoin="round"/></svg>
    <svg class="band" width="490" height="64" viewBox="0 0 490 64"><path d="M0 16 Q40 0 90 14 Q140 28 200 12 Q250 0 300 14 Q360 30 420 12 Q460 2 490 14 L490 64 L0 64 Z" fill="var(--band)"/></svg>
    <div class="dog-photo" role="img" aria-label="Photo of a golden retriever"></div>
    <div class="chews-photo" role="img" aria-label="Photo of three filled chew treats"></div>
    <span class="support">SUPOPORT FOR DOG</span>
    <div class="count"><div class="count__main">60 CHEWS</div><div class="count__net">NET WT 5.29 oz (150g)</div></div>
    <div class="flavor">
      <span class="flavor__icon"><svg width="26" height="18" viewBox="0 0 26 18"><ellipse cx="13" cy="9" rx="11" ry="7" fill="none" stroke="var(--white)" stroke-width="1.4"/><circle cx="9" cy="8" r="2.5" fill="none" stroke="var(--white)" stroke-width="1.2"/></svg></span>
      <span class="flavor__name">BEEF<br>LAVOR</span>
    </div>
  </section>

</main>
</body>
</html>
```